Pagevoより「最前線・空腹がすっと静まる献立&噛み方の手引き」というタイトルの電子書籍を出版予定です。

この本のコンセプトは「食べ物を選んで食べること&その食べ方で食欲が自然におさまること、更にはそれがダイエットと健康維持とアンチエイジングに非常に効果的であること、プラス今流行りのダイエット方(オートファジーダイエット、ミトコンドリア活性化、ケトジェニックダイエット、16時間断食、レクチンフリー 食品の勧め、腸活、SATエクササイズ、オイルの種類など)の説明とご提案(やり方)」をお伝えし、読者の皆様の健康維持に貢献したいということです。

ターゲットは男女ともに考えております。デザインは明るくて「何これ、ダイエットや食品の本にしては発想が新しい!」と興味を持ってもらえることを期待しております。(抽象的ですみません;)

何かご質問・ご提案がありましたらいつでもご連絡ください。
どうぞ宜しくお願いいたします。
*以下2項目の追加記載をお願いいたします。お手数ですがどうぞ宜しくお願いいたします。

・読者プレゼント
星座タイプ別 きみに向く減量術と献立チェック

・著者名: 森川 結奈
皆様、お忙しいところをたくさんのご応募、ありがとうございました!
どれも素敵なデザインでなかなか決めるのが難しいところではありますが、
数日中に決定、上位3名の方にご連絡いたします。

それでは、どうぞしばらくお待ちくださいませ。

取り急ぎ、お礼まで。

Thank you so much!
森川 結奈

当選:miru72_studio様 ー 明るくてフレッシュで清潔感のあるイメージで、何だろう?と書店だったら思わず手に取りたくなる素敵なデザインだと思いました。 次点:ripple_308様 ー デザインが可愛いく親しみやすいのと「食事を抑えるのでなく食欲を抑えるダイエット」など刺さるコピーがとても鋭いと感じました。執筆仲間にも好評でした。 次点: Hnbrook様 ー シンプルで見やすいが故に、逆に何が書いてあるんだろう?と興味を持たせてくれそうなデザインだと感じました。仲間内でも好評でした。

選定が遅くなり大変申し訳ございませんでした。この度は沢山の素敵なデザインをご提案くださり、ありがとうございました。 周りの者と相談の上、悩んだ末に決定させていただきました。 本当に素晴らしい作品ばかりで、デザインをするお仕事の素晴らしさを教えていただきました。 皆様のパワーにインスパイアされ、また二冊目も書きたいと思う原動力をいただきました。 またぜひご縁をいただけたら幸いです。 心より感謝申し上げます。どうもありがとうございました。 皆様のますますのご活躍とご発展をお祈り申し上げます。森川結奈

```html
<!DOCTYPE html>
<html lang="ja">
<head>
<meta charset="utf-8">
<title>最前線・空腹がすっと静まる献立&amp;噛み方の手引き</title>
<link href="https://fonts.googleapis.com/css2?family=Noto+Sans+JP:wght@500;700;900&display=swap" rel="stylesheet">
<style>
  :root {
    --red: #c8161d;
    --ink: #1c1c1c;
    --paper: #ffffff;
    --photo-warm: #e9cdbf;
    --photo-pink: #d98c8c;
    --photo-cream: #f4ece6;
  }
  html, body { margin: 0; padding: 0; overflow: hidden; background: #eee; }
  .cover {
    position: relative;
    width: 750px; height: 1200px;
    background: var(--paper);
    overflow: hidden;
    font-family: "Noto Sans JP", sans-serif;
    color: var(--ink);
  }
  .photo {
    position: absolute; left: 0; top: 420px; width: 750px; height: 600px;
    background:
      linear-gradient(180deg, var(--paper) 0%, rgba(255,255,255,0) 18%, rgba(255,255,255,0) 82%, var(--paper) 100%),
      radial-gradient(ellipse at 15% 40%, var(--photo-pink) 0%, rgba(217,140,140,0) 45%),
      radial-gradient(ellipse at 45% 45%, var(--photo-warm) 0%, rgba(233,205,191,0) 60%),
      linear-gradient(90deg, var(--photo-warm) 0%, var(--photo-cream) 70%, var(--paper) 100%);
  }
  .series-tab {
    position: absolute; left: 400px; top: 0; width: 175px; height: 88px;
    background: var(--red); border-radius: 0 0 16px 16px;
    color: #fff; font-weight: 900; font-size: 38px;
    display: flex; align-items: center; justify-content: center; letter-spacing: 2px;
  }
  .subtitle {
    position: absolute; top: 112px; left: 360px;
    display: flex; flex-direction: row-reverse; gap: 20px;
  }
  .subtitle span {
    writing-mode: vertical-rl; font-weight: 900; font-size: 50px; line-height: 1;
    letter-spacing: 4px; color: var(--ink);
  }
  .title {
    position: absolute; margin: 0;
    color: var(--red); font-weight: 900; line-height: 1; white-space: nowrap;
  }
  .title .amp { font-size: 0.66em; }
  .title-row1 { left: 40px; top: 70px; font-size: 150px; }
  .title-row2 { left: 120px; top: 345px; font-size: 140px; }
  .title-row3 { right: 30px; top: 545px; font-size: 130px; }
  .title-row3 .small { font-size: 72px; margin-right: 6px; }
  .author {
    position: absolute; left: 650px; top: 750px;
    writing-mode: vertical-rl; font-weight: 500; font-size: 36px; letter-spacing: 6px;
    color: var(--ink); line-height: 1;
  }
  .gift-label {
    position: absolute; left: 25px; top: 1022px; width: 212px; height: 50px;
    background: var(--ink); color: #fff; font-weight: 900; font-size: 28px;
    display: flex; align-items: center; justify-content: center;
  }
  .gift-line1 {
    position: absolute; left: 258px; top: 1018px; font-weight: 700; font-size: 40px; line-height: 1.4; color: var(--ink);
  }
  .gift-accent {
    position: absolute; left: 30px; top: 1095px; font-weight: 900; font-size: 30px; color: var(--red);
    transform: rotate(-10deg); transform-origin: left center; line-height: 1.15;
  }
  .gift-line2 {
    position: absolute; left: 170px; top: 1090px; font-weight: 900; font-size: 56px; line-height: 1.3; color: var(--ink);
    white-space: nowrap;
  }
</style>
</head>
<body>
<div class="cover">
  <div class="photo" role="img" aria-label="お茶碗のご飯を箸で口に運ぶ女性の写真"></div>

  <div class="series-tab">最前線</div>

  <div class="subtitle">
    <span>空腹が</span>
    <span>すっと</span>
    <span>静まる</span>
  </div>

  <h1 class="title title-row1">献立</h1>
  <div class="title title-row2"><span class="amp">&amp;</span>噛み方</div>
  <div class="title title-row3"><span class="small">の</span>手引き</div>

  <div class="author">森川 結奈</div>

  <div class="gift-label">読者プレゼント</div>
  <div class="gift-line1">星座タイプ別</div>
  <div class="gift-accent">きみに<br>向く</div>
  <div class="gift-line2">減量術と献立チェック</div>
</div>
</body>
</html>
```